Word template Letterhead for Australian Law Firm

We are a small law firm based in Manly, NSW, Australia. We have had a new logo designed for us and wish to freshen up the appearance of our letterhead. We require the letterhead to be in a word document that we can type over. This will not be a ‘printed’ letterhead because we send the majority of our correspondence via email. We would like to see a few options. We have attached our previous letterhead as well as the artwork for our new logo. We like the idea of a watermark across the bottom of the letter but the watermark must stay in place and we must be able to type over it. We are open to some colour throughout the letterhead because the majority of our correspondence is sent electronically. We also use electronic signatures. I have uploaded an example of this.The letterhead must include:-1. Our address details – including our phone number, physical address, website address etc. These details can be found on the copy of our previous letterhead;2. ABN Number;3. The words ‘Brevicor (NSW) Pty Ltd ACN 482 731 058 trading as Shipton & AssociatesLiability limited by a scheme approved under Professional Standards Legislation. The letterhead does not need to include the names and qualifications of the people working at the firm. Thank you.

Target Market(s)

Clients and other parties

Industry/Entity Type

Law Firm

Font styles to use
Other font styles liked:
• raleway, montserrat

Colors

Designer to choose colors to be used in the design.

Requirements
Must have
• Certain wording - please see project description.
• Must be a word document and must be able to type over the watermark etc.
Nice to have
• Watermark at the bottom of the letter.

```html
<!DOCTYPE html>
<html lang="en">
<head>
<meta charset="utf-8">
<title>Kervell &amp; Associates Letterhead</title>
<link rel="stylesheet" href="https://fonts.googleapis.com/css2?family=Jost:ital,wght@0,400;0,500;0,600;0,700;1,500;1,600&display=swap">
<style>
  :root {
    --ink: #111111;
    --brand-blue: #2f4fd8;
    --watermark: #e4e6eb;
    --badge-blue: #3a8ee8;
    --sig-tone: #d9d9d9;
    --paper: #ffffff;
  }
  html, body { margin: 0; padding: 0; overflow: hidden; background: var(--paper); }
  .letter {
    position: relative; width: 979px; height: 1200px; overflow: hidden;
    background: var(--paper); color: var(--ink);
    font-family: "Jost", Arial, sans-serif;
  }
  .letter > * { position: absolute; margin: 0; }
  .watermark { left: 0; right: 0; top: 768px; text-align: center; color: var(--watermark);
    font-size: 52px; font-weight: 600; letter-spacing: 3px; line-height: 1; z-index: 0; }
  .brand-mark { left: 24px; top: 92px; display: flex; align-items: center; gap: 8px; z-index: 1; }
  .brand-mark .dot { width: 20px; height: 20px; border-radius: 50%; background: var(--brand-blue); }
  .brand-mark .name { font-size: 16px; font-weight: 600; color: var(--brand-blue); letter-spacing: .5px; }
  .masthead { left: 266px; top: 46px; line-height: 1; font-weight: 700; }
  .masthead .kicker { font-size: 40px; display: block; }
  .masthead .firm { font-size: 46px; display: block; margin-top: 4px; letter-spacing: .5px; }
  .rule { left: 19px; right: 19px; top: 155px; border-top: 3px solid var(--ink); }
  .staff { left: 58px; top: 166px; font-size: 18px; font-weight: 600; line-height: 29px; }
  .contact { right: 57px; top: 171px; text-align: right; font-size: 17px; line-height: 25.5px; }
  .contact .strong { font-weight: 700; }
  .contact .web { font-weight: 600; }
  .recipient { left: 57px; top: 354px; font-size: 18px; font-weight: 600; line-height: 29px; font-style: normal; }
  .refs { right: 57px; top: 354px; text-align: right; font-size: 18px; font-weight: 700; line-height: 29px; }
  .dated { right: 57px; top: 424px; text-align: right; font-size: 16.5px; line-height: 23px; }
  .dated em { font-weight: 600; }
  .salutation { left: 45px; top: 499px; font-size: 16px; }
  .subject { left: 45px; top: 533px; font-size: 18px; font-weight: 600; }
  .body-copy { left: 57px; width: 865px; top: 594px; font-size: 18px; line-height: 29.7px; z-index: 1; }
  .body-copy .line { display: block; white-space: nowrap; text-align: justify; text-align-last: justify; }
  .body-copy .line.first { padding-left: 67px; }
  .body-copy .line.last { text-align-last: left; }
  .body-copy .para2 { margin-top: 24px; }
  .body-copy .para2 .first { padding-left: 16px; text-align-last: left; }
  .body-copy .para2 .last { padding-left: 24px; }
  .sign-off { left: 45px; top: 912px; font-size: 16.5px; line-height: 19px; z-index: 1; }
  .sign-off strong { display: block; font-size: 18px; font-weight: 600; line-height: 20px; }
  .sign-off small { display: block; font-size: 12px; margin-top: 2px; }
  .signature { left: 51px; top: 1004px; width: 184px; height: 70px; border-radius: 6px;
    background: linear-gradient(90deg, var(--sig-tone), #efefef); }
  .accreditation { left: 711px; top: 906px; }
  .footer { left: 0; right: 0; top: 1131px; text-align: center; font-size: 14px; line-height: 20px; }
  .footer em { display: block; }
</style>
</head>
<body>
<main class="letter">
  <div class="watermark" aria-hidden="true">Kervell &amp; Associates</div>

  <div class="brand-mark"><span class="dot"></span><span class="name">Kervell &amp; Associates</span></div>
  <h1 class="masthead"><span class="kicker">Solicitors</span><span class="firm">KERVELL &amp; ASSOCIATES</span></h1>
  <div class="rule"></div>

  <div class="staff">
    <div><em>Principal IPL:</em> R. HALVORSEN BA LLB, Acc Spec (Fam)</div>
    <div><em>Consultant:</em> D. A. KERVELL, BCom, LLM, Acc Spec (Fam)</div>
    <div><em>Senior Associate:</em> P. K. REDWAY, BA</div>
    <div><em>Associate:</em> T. PELLING, BA GDLP</div>
  </div>

  <div class="contact">
    <div>SUITE 4, 18 HARLOW STREET</div>
    <div>TARWICK NSW 2187</div>
    <div class="strong">TELEPHONE: (02) 9000 4817</div>
    <div>FACSIMILE: (02) 9000 4818</div>
    <div>EMAIL: reception@brevicorlaw.com.au</div>
    <div>ABN: 48 273 105 812</div>
    <div class="web">www.kervellandassociates.com.au</div>
  </div>

  <address class="recipient">
    <div>Kervell &amp; Associates</div>
    <div>Suite 4, 18 Harlow Street</div>
    <div>TARWICK NSW 2187</div>
  </address>

  <div class="refs">
    <div>OUR REF: RH:CLR:4821</div>
    <div>YOUR REF:Tom Varley</div>
  </div>
  <div class="dated">
    <div>9 September 2019</div>
    <div><em>By email only: xxx@xxx.com.au</em></div>
  </div>

  <p class="salutation">Dear Sir/Madam,</p>
  <p class="subject">RE: LOREM IPSUM DOLOR SIT AMET</p>

  <div class="body-copy">
    <p class="para1" style="margin:0">
      <span class="line first">Lorem ipsum dolor sit amet, consectetuer a iscing elit, sed diam nonummy nibh euismo</span>
      <span class="line">ncidunt ut laoreet dolore magna aliquam er olutpat. Ut wi si enim ad minim veniam, qui strud</span>
      <span class="line">exerci tation ullamcorper suscipit lob autem vel eum iriure dolor in hen drerit in tate velit esse</span>
      <span class="line">molestie consequat, vel illu re eu feugiat nulla facilisis at vero eros et an et iusto odio dignissim</span>
      <span class="line">qui blandit praes`ptatum zzril delenit augue duis dolore te f nulla facilisi. Nam liber tempor</span>
      <span class="line">cum soluta eleifend option congue nihil imperdiet dom quod mazim placerat facer possim assum.</span>
      <span class="line last">n habent claritatem insitam; est usus lege</span>
    </p>
    <p class="para2" style="margin-bottom:0">
      <span class="line first">Lorem ipsum dolor sit amet, consectetuer a iscing elit, sed diam nonummy nibh euismo</span>
      <span class="line last">ncidunt ut laoreet dolore magna aliquam er olutpat.</span>
    </p>
  </div>

  <div class="sign-off">
    <div>Yours faithfully</div>
    <strong>KERVELL &amp; ASSOCIATES</strong>
    <strong>ELAINE HALVORSEN</strong>
    <small>Direct Email: elaine@brevicorlaw.com.au</small>
  </div>
  <div class="signature" role="img" aria-label="Handwritten electronic signature of Elaine Halvorsen"></div>

  <svg class="accreditation" width="176" height="176" viewBox="0 0 176 176" aria-hidden="true">
    <circle cx="88" cy="88" r="84" fill="none" stroke="var(--ink)" stroke-width="3"/>
    <circle cx="88" cy="88" r="54" fill="var(--badge-blue)"/>
  </svg>

  <footer class="footer">
    Brevicor (NSW) Pty Ltd ACN 482 731 058 trading as Kervell &amp; Associates
    <em>Liability limited by a scheme approved under Professional Standards Legislation. Legal practitioners at</em>
    <em>Brevicor (NSW) Pty Ltd are members of the scheme.</em>
  </footer>
</main>
</body>
</html>
```